Award winning Indie press looking for a world class book cover for global relaunch

We need to update a book cover for one of our titles which is being relaunched. The title will exist in both physical and e-formats.
The book is genre specific and era specific. World war 2, Greece. Beyond the Quiet Hills is a compelling work of literary fiction, a war novel that explores the challenges of peace. A gripping historical adventure, it paints a portrait of courage and love in the fatal shadow of global conflict that has spilled into the twenty-first century.
Usage of the provided images is of course optional but it is a book about the German occupation of Greece. Images are public domain.
The cover needs to convey a sense of drama, typical for war novels.
Necessary information.
Size: A5
Title: Beyond the Quiet Hills
Author: Martin Hollowell
Blurb: An excellent book - Brackwater Review UK
Publisher: logo- provided
Spine: Spine: 0.785 inches or 19.93 mm
Back cover text: Occupied Greece 1943. Beyond the Quiet Hills is a compelling work of literary fiction, a war novel that also explores the challenges of peace. A gripping historical adventure, it paints a portrait of courage and love in the fatal shadow of global conflict that has spilled tragically into the twenty-first century.
Citizens of Nazi-occupied Greece face daily decisions that affect their freedom and their survival. When music teacher Lefteris intervenes in a dispute between a Greek woman and a German soldier, he and jazz singer Nina are plunged into the brutal world of armed resistance.
Owen Rutledge, a British agent, lands in Northern Greece, where he joins Lefteris’ and Nina’s network. Never fully understanding his Greek collaborators, he forms a deep bond with them.
In Scotland after World War Two, Owen is alienated from everyday life until he meets Maud, an up and coming intelligence officer. Surrounded by opportunity and courted by influential mentors, Owen and Maud learn that integrity has to be fought for in peacetime Britain just as in wartime Europe.
When Owen undertakes a final mission to Greece, now in the full throes of civil war, the weight of ideology and history descends with sudden force on the small town where former friends and enemies confront one another in a terrifying climax.
Please allow approximately 2cm height X 3 cm length for the bar code.
Reason: Decided to allow more time as this is proving a bit more tricky than expected.

```html
<!DOCTYPE html>
<html lang="en">
<head>
<meta charset="utf-8">
<title>Beyond the Quiet Hills — Martin Hollowell</title>
<link rel="stylesheet" href="https://fonts.googleapis.com/css2?family=Cinzel:wght@400&family=Caveat:wght@700&family=Tinos:ital,wght@0,700;1,700&family=Open+Sans:wght@600&display=swap">
<style>
  :root {
    --page: #ffffff;
    --cover: #1f1d1e;
    --ink-light: #ffffff;
    --accent-red: #d4111e;
    --rule: #ffffff;
    --frame: #111111;
    --photo-light: #cfcdc6;
    --photo-mid: #9a9a96;
    --photo-dark: #5e6166;
    --flag-blue: #4f7fb8;
    --flag-white: #ece8df;
  }
  * { margin: 0; padding: 0; box-sizing: border-box; }
  html, body {
    width: 838px; height: 1200px; overflow: hidden;
    background: var(--page);
  }
  .cover {
    position: absolute; left: 25px; top: 28px;
    width: 787px; height: 1138px;
    background: var(--cover);
    border: 1px solid var(--frame);
    overflow: hidden;
  }
  .author {
    position: absolute; left: 0; right: 0; top: 40px;
    text-align: center;
    font-family: "Cinzel", "Times New Roman", serif;
    color: var(--ink-light);
    line-height: 1;
    font-weight: 400;
  }
  .author-first { display: block; font-size: 76px; letter-spacing: 2px; }
  .author-last  { display: block; font-size: 110px; letter-spacing: 0; margin-top: 8px; }
  .title {
    position: absolute; left: 0; right: 0; top: 252px;
    text-align: center;
    font-family: "Caveat", "Comic Sans MS", cursive;
    font-weight: 700;
    font-size: 84px;
    color: var(--accent-red);
    line-height: 1;
    letter-spacing: 2px;
  }
  .title-rule {
    position: absolute; left: 0; right: 0; top: 347px;
    height: 8px; background: var(--rule);
  }
  .cover-art {
    position: absolute; left: 0; top: 366px;
    width: 787px; height: 626px;
  }
  .flag-blue  { fill: var(--flag-blue); }
  .flag-white { fill: var(--flag-white); }
  .review {
    position: absolute; left: 22px; top: 1012px;
    font-family: "Tinos", "Times New Roman", serif;
    font-size: 19px; font-weight: 700;
    color: var(--ink-light);
  }
  .review cite { font-style: italic; }
  .publisher {
    position: absolute; left: 22px; top: 1060px;
    width: 190px; height: 44px;
    background: var(--accent-red);
    display: flex; align-items: center; justify-content: center;
    font-family: "Open Sans", Arial, sans-serif;
    font-weight: 600; font-size: 31px;
    color: var(--ink-light);
    letter-spacing: 1px;
  }
  .barcode-space {
    position: absolute; left: 600px; top: 1003px;
    width: 160px; height: 107px;
    background: var(--ink-light);
  }
</style>
</head>
<body>
  <main class="cover">
    <h1 class="author">
      <span class="author-first">MARTIN</span>
      <span class="author-last">HOLLOWELL</span>
    </h1>
    <h2 class="title">Beyond the Quiet Hills</h2>
    <div class="title-rule"></div>

    <svg class="cover-art" viewBox="0 0 787 626" role="img"
         aria-label="Weathered Greek flag blended with a wartime photograph of occupying troops marching before an ancient temple">
      <defs>
        <linearGradient id="photoTone" x1="0" y1="0" x2="0.2" y2="1">
          <stop offset="0" stop-color="var(--photo-light)"/>
          <stop offset="0.55" stop-color="var(--photo-mid)"/>
          <stop offset="1" stop-color="var(--photo-dark)"/>
        </linearGradient>
        <clipPath id="artShape">
          <polygon points="0,0 787,0 787,626 0,468"/>
        </clipPath>
      </defs>
      <g clip-path="url(#artShape)">
        <rect width="787" height="626" fill="url(#photoTone)"/>
        <g class="flag" opacity="0.72" transform="rotate(-7 400 300)">
          <rect class="flag-white" x="-120" y="-60" width="1100" height="80"/>
          <rect class="flag-blue"  x="-120" y="20"  width="1100" height="80"/>
          <rect class="flag-white" x="-120" y="100" width="1100" height="80"/>
          <rect class="flag-blue"  x="-120" y="180" width="1100" height="80"/>
          <rect class="flag-white" x="-120" y="260" width="1100" height="80"/>
          <rect class="flag-blue"  x="-120" y="340" width="1100" height="80"/>
          <rect class="flag-white" x="-120" y="420" width="1100" height="80"/>
          <rect class="flag-blue"  x="-120" y="500" width="1100" height="80"/>
          <rect class="flag-white" x="-120" y="580" width="1100" height="80"/>
          <rect class="flag-blue"  x="-120" y="-60" width="420" height="400"/>
          <rect class="flag-white" x="-120" y="100" width="420" height="80"/>
          <rect class="flag-white" x="50"   y="-60" width="80"  height="400"/>
        </g>
      </g>
    </svg>

    <p class="review">“An excellent book” <cite>(Brackwater Review UK)</cite></p>
    <div class="publisher">TESSARO</div>
    <div class="barcode-space"></div>
  </main>
</body>
</html>
```